Morvex Business Card (intended for Business Card sized magnet)

Hi guys,

I would like to get a design for my business card for the restaurant. The design must be single sided as I intend to produce business card sized magnets.

The File attached must me on and I'm open for new ides

Can you please ensure that the design meets Cardowell's magnetic business card size specifications:

http://www.cardowell.example.au/custom-magnets.aspx?txi=15695&xnid=TopNav_Magnetic+Business+Cards+(linked+item)_Magnets_Marketing+Products&xnav=TopNav

Full Bleed Size (starting document size):
90 x 52 mm
1062 x 615 pixels
* Finished artwork should use the full bleed dimensions for best results.

Document Trim Size (final size after being cut):
87 x 49 mm
1028 x 579 pixels
* Please be sure to keep all text within the safe margin.

Resolution:
300 DPI

The winning design/source files need to meet these specifications.

Thanks
Updates

Hi guys, can I see more options please Thanks

```html
<!DOCTYPE html>
<html lang="en">
<head>
<meta charset="utf-8">
<title>Morvex Business Card</title>
<link href="https://fonts.googleapis.com/css2?family=Crimson+Text&family=Open+Sans:wght@400&display=swap" rel="stylesheet">
<style>
  :root {
    --backdrop: #e9e9eb;
    --card: #ffffff;
    --pattern-light: #f6f6f7;
    --pattern-mid: #e8e8ea;
    --brand-blue: #1a469b;
    --text-dark: #3f3f44;
    --rule: #d9d9dc;
  }
  * { box-sizing: border-box; margin: 0; padding: 0; }
  html, body {
    width: 1200px; height: 1200px; overflow: hidden;
    background: var(--backdrop);
  }
  .canvas {
    width: 1200px; height: 1200px;
    display: flex; flex-direction: column; align-items: center; justify-content: center;
    gap: 60px;
  }
  .card {
    position: relative;
    width: 860px; height: 484px;
    background: var(--card);
    overflow: hidden;
    box-shadow: 0 6px 18px rgba(0,0,0,0.12);
  }
  .card-texture {
    position: absolute; inset: 0;
    background: linear-gradient(135deg, var(--pattern-light), var(--pattern-mid) 50%, var(--pattern-light));
  }
  .wordmark {
    font-family: "Crimson Text", Georgia, serif;
    font-weight: 400;
    color: #ffffff;
    font-size: 64px;
    letter-spacing: 1px;
    line-height: 1;
  }
  /* Front */
  .front-band {
    position: absolute; left: 0; right: 0; top: 84px; height: 200px;
    background: var(--brand-blue);
    display: flex; align-items: center; justify-content: center;
  }
  /* Back */
  .back-stripe {
    position: absolute; left: 0; right: 0; height: 3px; background: var(--rule);
  }
  .scallop { position: absolute; inset: 0; }
  .back-wordmark {
    position: absolute; left: 330px; width: 420px; top: 62px; text-align: center;
  }
  .contact {
    position: absolute; left: 0; right: 0; top: 300px;
    display: flex; justify-content: center;
    font-family: "Open Sans", Arial, sans-serif;
    color: var(--text-dark);
    font-size: 22px; line-height: 1.45;
  }
  .contact-address {
    text-align: right; padding-right: 22px;
    border-right: 2px solid var(--text-dark);
  }
  .contact-lines { padding-left: 22px; list-style: none; }
  .contact-lines li { display: flex; align-items: center; gap: 10px; }
  .contact-icon { width: 20px; height: 20px; flex: none; }
</style>
</head>
<body>
<main class="canvas">

  <section class="card card-front" aria-label="Card front">
    <div class="card-texture" role="img" aria-label="Faint grey geometric star pattern"></div>
    <div class="front-band">
      <span class="wordmark">Morvex</span>
    </div>
  </section>

  <section class="card card-back" aria-label="Card back with contact details">
    <div class="card-texture" role="img" aria-label="Faint grey geometric star pattern"></div>
    <div class="back-stripe" style="top:230px"></div>
    <div class="back-stripe" style="top:410px"></div>
    <svg class="scallop" viewBox="0 0 860 484" aria-hidden="true">
      <g fill="#1a469b">
        <rect x="340" y="0" width="400" height="150"/>
        <circle cx="340" cy="30" r="40"/>
        <circle cx="335" cy="100" r="42"/>
        <circle cx="385" cy="155" r="45"/>
        <circle cx="465" cy="170" r="45"/>
        <circle cx="545" cy="175" r="45"/>
        <circle cx="625" cy="170" r="45"/>
        <circle cx="700" cy="155" r="45"/>
        <circle cx="745" cy="100" r="42"/>
        <circle cx="740" cy="30" r="40"/>
      </g>
    </svg>
    <div class="back-wordmark"><span class="wordmark">Morvex</span></div>

    <div class="contact">
      <address class="contact-address" style="font-style:normal">
        412 Harlow park road<br>ashvale north, 3190
      </address>
      <ul class="contact-lines">
        <li>
          <svg class="contact-icon" viewBox="0 0 20 20" aria-hidden="true">
            <circle cx="10" cy="10" r="10" fill="#1a469b"/>
            <rect x="7" y="4.5" width="6" height="11" rx="1.2" fill="#fff"/>
          </svg>
          03 5501 2487
        </li>
        <li>
          <svg class="contact-icon" viewBox="0 0 20 20" aria-hidden="true">
            <circle cx="10" cy="10" r="10" fill="#1a469b"/>
            <rect x="5" y="6.5" width="10" height="7" fill="#fff"/>
            <path d="M5 6.5 L10 10.5 L15 6.5" stroke="#1a469b" stroke-width="1" fill="none"/>
          </svg>
          morvex678@mailbox.example
        </li>
        <li>
          <svg class="contact-icon" viewBox="0 0 20 20" aria-hidden="true">
            <circle cx="10" cy="10" r="10" fill="#1a469b"/>
            <circle cx="10" cy="10" r="5.5" fill="none" stroke="#fff" stroke-width="1.2"/>
            <path d="M4.5 10 H15.5 M10 4.5 V15.5" stroke="#fff" stroke-width="1.2"/>
          </svg>
          www.morvex.example.au
        </li>
      </ul>
    </div>
  </section>

</main>
</body>
</html>
```